Letterhead

We are looking for a basic letterhead. It should include our logo, website - northpeakkitchenware.com, phone 907.418.3952, toll free 855.392.6180, and fax 907.418.5263, along with our address 4837 Birchwood Lane, Anchorage, AK 99517. I want something that will look good printed in color or black and white.

```html
<!DOCTYPE html>
<html lang="en">
<head>
<meta charset="UTF-8">
<title>North Peak Kitchenware – Letterhead</title>
<link href="https://fonts.googleapis.com/css2?family=Open+Sans:wght@400;600;700&family=PT+Serif:wght@400&display=swap" rel="stylesheet">
<style>
  :root {
    --navy: #1d3a78;
    --red: #c32739;
    --ink: #2b2b2b;
    --muted: #4a4a4a;
    --paper: #ffffff;
    --backdrop: #eeeeee;
    --footer-text: #ffffff;
  }
  * { margin: 0; padding: 0; box-sizing: border-box; }
  html, body {
    width: 1084px;
    height: 1200px;
    overflow: hidden;
    background: var(--backdrop);
  }
  .letterhead {
    position: absolute;
    left: 132px;
    top: 12px;
    width: 820px;
    height: 1175px;
    background: var(--paper);
    font-family: "Open Sans", Arial, sans-serif;
    color: var(--ink);
  }
  .brand {
    position: absolute;
    top: 128px;
    left: 0;
    width: 100%;
    text-align: center;
    color: var(--navy);
    font-weight: 700;
  }
  .brand-name {
    display: block;
    font-size: 44px;
    line-height: 1;
    letter-spacing: 0.5px;
  }
  .brand-sub {
    display: block;
    margin-top: 6px;
    font-size: 17px;
    letter-spacing: 3px;
  }
  .salutation {
    position: absolute;
    left: 113px;
    top: 278px;
    font-size: 19px;
  }
  .letter-body {
    position: absolute;
    left: 113px;
    top: 362px;
    width: 610px;
    font-size: 16.6px;
    line-height: 27.6px;
    text-align: justify;
    hyphens: auto;
    color: var(--muted);
  }
  .letter-body p + p { margin-top: 28px; }
  .signature {
    position: absolute;
    left: 113px;
    top: 948px;
  }
  .signature-name { font-size: 18px; color: var(--ink); }
  .signature-title { font-size: 13px; color: var(--muted); margin-top: 6px; }
  .footer-bands {
    position: absolute;
    left: 0;
    bottom: 0;
    width: 820px;
    height: 89px;
  }
  .footer-text {
    position: absolute;
    font-family: "PT Serif", Georgia, serif;
    font-style: normal;
    font-size: 12px;
    line-height: 17px;
    color: var(--footer-text);
  }
  .footer-address { left: 97px; top: 1127px; text-align: center; }
  .footer-phones { left: 367px; top: 1127px; }
  .footer-web { left: 597px; top: 1136px; }
  .tollfree {
    position: absolute;
    left: 500px;
    top: 1086px;
    height: 31px;
    line-height: 31px;
    color: var(--navy);
    font-family: "Open Sans", Arial, sans-serif;
    white-space: nowrap;
  }
  .tollfree-label { font-size: 15px; }
  .tollfree-number { font-size: 23px; font-weight: 700; margin-left: 4px; }
</style>
</head>
<body>
  <main class="letterhead">
    <header class="brand">
      <span class="brand-name">NORTH PEAK</span>
      <span class="brand-sub">KITCHENWARE</span>
    </header>

    <p class="salutation">Dear Mr. Smith,</p>

    <section class="letter-body">
      <p>Lorem ipsum dolor sit amet, consectetur adipiscing elit. Donec orci purus, luctus vitae dignissim eu, iaculis sed purus. Vivamus faucibus, ipsum nec aliquet viverra, leo mauris condimentum ligula, sit amet sagittis enim ligula quis arcu. Nam egestas tortor id nisi porttitor mattis. In tortor ante, ultricies in suscipit a, tempus non massa. Vivamus et auctor mi. Fusce vel massa nulla. Phasellus nec eros mauris, et scelerisque orci. Donec malesuada orci vitae nulla accumsan porta a id massa. Quisque accumsan iaculis magna sit amet fringilla. Maecenas consequat, magna eget tincidunt semper, odio nibh rutrum mi, id feugiat ante nisi eu risus. Vestibulum nunc orci, rhoncus a placerat in, ultricies in mi. Cras mattis varius eros, vel fringilla nisi suscipit eget.</p>
      <p>Quisque scelerisque sagittis nulla at porttitor. Mauris a justo et tellus interdum tristique. Sed id augue vitae urna euismod commodo aliquet a quam. Pellentesque arcu velit, cursus et malesuada ut, consequat et diam. Nullam erat sem, rhoncus id ullamcorper vitae, rhoncus et arcu. In ultricies ultricies nulla, ut rutrum nisi iaculis at. Donec eu magna a metus ornare faucibus. Fusce aliquet faucibus ultricies. Morbi semper, est id tincidunt gravida, sem arcu adipiscing lacus, ac bibendum nulla leo eu purus. Quisque nec diam sed risus consectetur a ccumsan quis quis nibh. Vestibulum id purus lorem.</p>
    </section>

    <div class="signature">
      <p class="signature-name">John Doe</p>
      <p class="signature-title">Co-Founder &amp; CEO</p>
    </div>

    <svg class="footer-bands" viewBox="0 0 820 89" aria-hidden="true">
      <polygon points="451,0 820,0 820,31 383,31" fill="var(--red)"/>
      <polygon points="87,31 820,31 820,84 0,84" fill="var(--navy)"/>
      <rect x="0" y="84" width="820" height="5" fill="var(--red)"/>
    </svg>

    <p class="tollfree"><span class="tollfree-label">free call</span><span class="tollfree-number">855.392.6180</span></p>

    <address class="footer-text footer-address">4837 Birchwood Lane,<br>Anchorage, AK 99517</address>
    <p class="footer-text footer-phones">t: 907.418.3952<br>f: 907.418.5263</p>
    <p class="footer-text footer-web">www.northpeakkitchenware.com</p>
  </main>
</body>
</html>
```